Business Card Design For Marketing Agnecy LVT

Need business card design for marketing agency.

Dorian Pell
President, CEO
1-555-304-2917
dorian@lumenvaletrewards.net
www.LumenValeTrewards.biz

Back Side:
Boost Sales Using Rewards, Incentives & Giveaways
Get A Free Sample Package

Target Market(s)

B2B

Industry/Entity Type

Marketing

Contact Information for Business Card

Dorian Pell
President, CEO
1-555-304-2917

Back Side:
Get A Free Sample Package

Please note that my current url is OLD DESIGN. I am working on new design and want the business card to match color themes at least on new site. Here is the demo link for new site so you can see the colors I use, etc.

http://pagekilnstudio.example/qx/dorian/lvt_final/index.html

Requirements
Must have
• Please note that my current url is OLD DESIGN. I am working on new design and want the business card to match color themes at least on new site. Here is the demo link for new site so you can see the colors I use, etc.

Nice to have

Should not have

```html
<!DOCTYPE html>
<html lang="en">
<head>
<meta charset="utf-8">
<title>LVT Business Card</title>
<link rel="stylesheet" href="https://fonts.googleapis.com/css2?family=Poppins:wght@400;500;600;700&family=Roboto:wght@400;500&display=swap">
<style>
  :root {
    --brand-blue: #1277c1;
    --ink-grey: #555a60;
    --paper: #ffffff;
    --stage: #2d2d2f;
  }
  html, body {
    margin: 0;
    padding: 0;
    width: 1200px;
    height: 900px;
    overflow: hidden;
    background: var(--stage);
  }
  .canvas {
    position: relative;
    width: 1200px;
    height: 900px;
  }
  .card {
    position: absolute;
    left: 320px;
    width: 560px;
    height: 320px;
    border-radius: 16px;
    overflow: hidden;
    box-sizing: border-box;
  }
  .card-back {
    top: 100px;
    background: var(--brand-blue);
    color: var(--paper);
    display: flex;
    flex-direction: column;
    align-items: center;
    justify-content: center;
    text-align: center;
  }
  .card-front {
    top: 470px;
    background: var(--paper);
  }

  .brand-mark {
    display: flex;
    align-items: center;
    gap: 10px;
    font-family: "Poppins", sans-serif;
    font-weight: 700;
    letter-spacing: 0.02em;
  }
  .brand-mark .dot {
    width: 14px;
    height: 14px;
    border-radius: 50%;
    background: currentColor;
    flex: none;
  }
  .card-back .brand-mark {
    font-size: 38px;
    color: var(--paper);
    margin-bottom: 26px;
  }
  .tagline {
    font-family: "Roboto", sans-serif;
    font-weight: 500;
    font-size: 16px;
    line-height: 1.35;
    margin: 0;
  }

  .card-front .brand-mark {
    position: absolute;
    top: 56px;
    right: 40px;
    font-size: 26px;
    color: var(--brand-blue);
  }
  .edge-tab {
    position: absolute;
    left: 0;
    top: 196px;
    width: 20px;
    height: 36px;
    background: var(--brand-blue);
    border-radius: 0 8px 8px 0;
  }
  .contact-block {
    position: absolute;
    left: 52px;
    top: 176px;
    font-family: "Poppins", sans-serif;
  }
  .person-name {
    margin: 0;
    font-size: 22px;
    font-weight: 700;
    color: var(--brand-blue);
    text-transform: uppercase;
    line-height: 1.1;
  }
  .person-role {
    margin: 2px 0 14px;
    font-size: 14px;
    font-weight: 600;
    color: var(--ink-grey);
  }
  .contact-list {
    list-style: none;
    margin: 0;
    padding: 0;
  }
  .contact-list li {
    display: flex;
    align-items: center;
    gap: 8px;
    font-size: 13px;
    color: var(--ink-grey);
    line-height: 1.55;
  }
  .contact-list svg {
    width: 13px;
    height: 13px;
    flex: none;
    fill: none;
    stroke: var(--brand-blue);
    stroke-width: 2;
  }
</style>
</head>
<body>
<main class="canvas">
  <section class="card card-back" aria-label="Card back">
    <div class="brand-mark"><span class="dot"></span>Lumen Vale Trewards</div>
    <p class="tagline">Boost Sales Using Rewards,<br>Incentives &amp; Giveaways Get A Free Sample Package<br>www.LumenValeTrewards.biz</p>
  </section>

  <section class="card card-front" aria-label="Card front">
    <div class="brand-mark"><span class="dot"></span>Lumen Vale Trewards</div>
    <span class="edge-tab"></span>
    <div class="contact-block">
      <h1 class="person-name">Dorian Pell</h1>
      <p class="person-role">President, CEO</p>
      <ul class="contact-list">
        <li>
          <svg viewBox="0 0 24 24" aria-hidden="true"><path d="M5 3h4l2 5-3 2a12 12 0 0 0 6 6l2-3 5 2v4a2 2 0 0 1-2 2A17 17 0 0 1 3 5a2 2 0 0 1 2-2z"/></svg>
          1-555-304-2917
        </li>
        <li>
          <svg viewBox="0 0 24 24" aria-hidden="true"><rect x="3" y="5" width="18" height="14" rx="2"/><path d="M3 7l9 6 9-6"/></svg>
          dorian@lumenvaletrewards.net
        </li>
        <li>
          <svg viewBox="0 0 24 24" aria-hidden="true"><circle cx="12" cy="12" r="9"/><path d="M3 12h18M12 3a14 14 0 0 1 0 18M12 3a14 14 0 0 0 0 18"/></svg>
          www.LumenValeTrewards.biz
        </li>
      </ul>
    </div>
  </section>
</main>
</body>
</html>
```